Birchlane Chiropractic Business Cards

Business cards with new logo design. Will upload copy of current card. We like the layout, but we need a new logo. Family, husband holding up baby toward sky, mom and other child standing next to him. We will probably want to include a catch phrase with logo. TBD

```html
<!DOCTYPE html>
<html lang="en">
<head>
<meta charset="utf-8">
<title>Birchlane Chiropractic Business Cards</title>
<link rel="stylesheet" href="https://fonts.googleapis.com/css2?family=Montserrat:wght@700;800&family=Arimo:wght@400&display=swap">
<style>
  :root {
    --backdrop: #2a2a2a;
    --card: #0b0b0b;
    --accent-red: #d8282e;
    --brand-blue: #1f5f9c;
    --text-light: #f2f2f2;
    --text-muted: #a8a8a8;
    --divider: #3a3a3a;
    --map-light: #ffffff;
    --map-shade: #e4e4e4;
  }
  * { margin: 0; padding: 0; box-sizing: border-box; }
  html, body { width: 1200px; height: 900px; overflow: hidden; }
  body {
    background: var(--backdrop);
    position: relative;
    font-family: "Arimo", Arial, sans-serif;
  }
  .card {
    position: absolute;
    top: 296px;
    width: 540px;
    height: 308px;
    background: var(--card);
    border-radius: 22px;
    overflow: hidden;
  }
  .card--front { left: 40px; }
  .card--back { left: 620px; }

  /* Front */
  .brand {
    position: absolute;
    left: 30px;
    top: 0;
    width: 196px;
    height: 100%;
    display: flex;
    flex-direction: column;
    justify-content: center;
    align-items: flex-start;
    gap: 14px;
  }
  .brand__dot {
    width: 42px;
    height: 42px;
    border-radius: 50%;
    background: var(--brand-blue);
  }
  .brand__name {
    font-family: "Montserrat", Arial, sans-serif;
    font-weight: 800;
    font-size: 22px;
    line-height: 1.08;
    color: var(--brand-blue);
    text-transform: uppercase;
    letter-spacing: 0.3px;
  }
  .divider {
    position: absolute;
    left: 236px;
    top: 62px;
    width: 1px;
    height: 184px;
    background: var(--divider);
  }
  .details {
    position: absolute;
    left: 256px;
    top: 82px;
    right: 16px;
  }
  .details__name {
    font-family: "Montserrat", Arial, sans-serif;
    font-weight: 700;
    font-size: 18px;
    color: var(--accent-red);
    text-transform: uppercase;
    white-space: nowrap;
  }
  .details__title {
    font-size: 15px;
    color: var(--text-muted);
    margin-top: 4px;
  }
  .contact { list-style: none; margin-top: 34px; }
  .contact__item {
    display: flex;
    align-items: center;
    gap: 8px;
    font-size: 15px;
    color: var(--text-muted);
    margin-bottom: 6px;
    white-space: nowrap;
  }
  .contact__icon { width: 13px; height: 13px; flex: none; }

  /* Back */
  .map-area {
    position: absolute;
    left: 165px;
    top: 24px;
    width: 210px;
    height: 160px;
    background: linear-gradient(160deg, var(--map-light), var(--map-shade));
  }
  .address {
    position: absolute;
    left: 0;
    right: 0;
    top: 204px;
    text-align: center;
    font-size: 15px;
    line-height: 1.35;
    color: var(--text-light);
  }
  .address__label { color: var(--accent-red); }
</style>
</head>
<body>
  <section class="card card--front">
    <div class="brand">
      <span class="brand__dot"></span>
      <p class="brand__name">Birchlane<br>Chiropractic</p>
    </div>
    <div class="divider"></div>
    <div class="details">
      <h1 class="details__name">Dr. Marcus W. Hale</h1>
      <p class="details__title">Chiropractic Physician</p>
      <ul class="contact">
        <li class="contact__item">
          <svg class="contact__icon" viewBox="0 0 24 24" aria-hidden="true"><path fill="#d8282e" d="M6.6 10.8a15.1 15.1 0 0 0 6.6 6.6l2.2-2.2a1 1 0 0 1 1-.25 11.4 11.4 0 0 0 3.6.57 1 1 0 0 1 1 1V20a1 1 0 0 1-1 1A17 17 0 0 1 3 4a1 1 0 0 1 1-1h3.5a1 1 0 0 1 1 1c0 1.25.2 2.45.57 3.57a1 1 0 0 1-.25 1z"/></svg>
          503-555-0148
        </li>
        <li class="contact__item">
          <svg class="contact__icon" viewBox="0 0 24 24" aria-hidden="true"><g fill="none" stroke="#d8282e" stroke-width="2"><circle cx="12" cy="12" r="10"/><ellipse cx="12" cy="12" rx="4.5" ry="10"/><path d="M2 12h20M4 6.5h16M4 17.5h16"/></g></svg>
          HaleChiropractic.com
        </li>
      </ul>
    </div>
  </section>

  <section class="card card--back">
    <div class="map-area" role="img" aria-label="Street map showing the clinic location between nearby avenues"></div>
    <p class="address">
      2840 SE Alder Crest Dr.<br>
      Maple Hollow, Oregon 97099<br>
      <span class="address__label">P:</span> 503-555-0148 &nbsp;<span class="address__label">F:</span> 503-555-0172
    </p>
  </section>
</body>
</html>
```